National commercial insurance agency needs design for email campaign to other insurance agencies ...

National commercial insurance agency needs design for email campaign to other insurance agencies needing to place workers comp policies and and also need very intense risk management. We want to market to smaller insurance agencies to refer us to their larger clients or prospects.

Font styles to use
Sans Serif

```html
<!DOCTYPE html>
<html lang="en">
<head>
<meta charset="utf-8">
<title>Ridgeway – Workers Comp Referral Campaign</title>
<link rel="stylesheet" href="https://fonts.googleapis.com/css2?family=Titillium+Web:wght@300;400;600;700&display=swap">
<style>
  :root{
    --orange:#f26b35;
    --orange-soft:#f4a37f;
    --ink:#333333;
    --ink-soft:#555555;
    --panel:#eef0ef;
    --white:#ffffff;
    --footer:#3d3d3d;
    --rule:#cfd2d1;
    --quote:#d6d8d7;
    --social:#5e8fd1;
  }
  *{box-sizing:border-box;margin:0;padding:0}
  html,body{width:1200px;height:4309px;overflow:hidden}
  body{font-family:"Titillium Web",Arial,sans-serif;color:var(--ink);background:var(--white);position:relative}
  .abs{position:absolute}

  /* wordmark */
  .brand{font-weight:700;font-size:56px;letter-spacing:1px;line-height:1;color:var(--white)}
  .hero-brand{right:97px;top:98px}

  /* hero */
  .hero{left:0;top:0;width:1200px;height:741px;
    background:linear-gradient(160deg,#8b8e90 0%,#b7b9ba 35%,#9c9fa1 60%,#6d7072 100%)}
  .hero-title{left:80px;top:458px;font-weight:300;font-size:41px;line-height:69px;color:var(--white)}
  .hero-title span{background:rgba(40,42,44,.72);padding:2px 12px 4px}

  /* pillars */
  .pillars{left:0;top:741px;width:1200px;height:288px;background:var(--orange);color:var(--white)}
  .pillar{top:76px;width:300px}
  .pillar h3{display:flex;align-items:center;gap:14px;font-weight:600;font-size:27px;letter-spacing:.5px;margin-bottom:14px}
  .pillar p{font-weight:600;font-size:20px;line-height:26px}

  /* panel */
  .panel{left:0;top:1029px;width:1200px;height:1514px;background:var(--panel)}
  .intro{left:59px;top:1105px;width:1073px;height:342px;background:var(--white);border-radius:40px;
    padding:60px 140px 0 67px;font-size:25px;line-height:27px;color:var(--ink)}
  .quote-mark{left:1030px;top:1180px;font-family:Georgia,serif;font-size:260px;line-height:1;color:var(--quote)}
  .section-title{left:0;top:1515px;width:1200px;text-align:center;font-size:36px;font-weight:400;color:var(--ink)}
  .section-rule{left:556px;top:1594px;width:88px;height:3px;background:var(--orange)}

  .grid-line-h{left:59px;top:2073px;width:1088px;height:2px;background:var(--rule)}
  .grid-line-v{width:2px;background:var(--rule)}
  .offer h4{font-weight:700;font-size:16px;letter-spacing:.5px;text-transform:uppercase;color:var(--ink);width:280px}
  .offer p{font-size:14px;line-height:19px;color:var(--ink-soft);width:270px}
  .photo{border-radius:32px}

  /* email draft */
  .draft{left:100px;top:2614px;width:994px;height:332px;border:3px solid var(--orange-soft);background:var(--white);text-align:center}
  .draft h2{margin-top:46px;font-weight:400;font-size:35px;color:var(--ink)}
  .draft p{margin:12px auto 0;width:710px;font-size:23px;line-height:31px;color:var(--ink)}
  .btn{display:inline-block;font-family:inherit}
  .btn-solid{left:529px;top:2855px;width:112px;height:47px;background:var(--orange);color:var(--white);font-size:22px;line-height:47px;text-align:center}

  /* feature card */
  .feature-bg{left:0;top:3013px;width:1200px;height:824px;background:var(--panel)}
  .feature{left:106px;top:3072px;width:976px;height:691px;background:var(--white);border:2px solid #c9cbca}
  .feature-photo{left:106px;top:3072px;width:976px;height:441px;background:linear-gradient(200deg,#e9eef2 0%,#b4bcc3 40%,#4d5257 75%,#2f3337 100%)}
  .feature-title{left:106px;top:3528px;width:976px;text-align:center;font-size:34px;font-weight:400;color:var(--ink)}
  .feature-text{left:106px;top:3583px;width:976px;text-align:center;font-size:23px;line-height:35px;color:var(--ink)}
  .btn-outline{left:514px;top:3681px;width:168px;height:50px;border:2px solid var(--orange-soft);color:var(--ink);font-size:22px;line-height:46px;text-align:center}

  /* footer */
  .footer-band{left:0;top:3837px;width:1200px;height:153px;background:var(--footer)}
  .footer-brand{left:59px;top:50px;font-size:52px}
  .social{top:57px;width:42px;height:42px;border-radius:6px;background:var(--social)}
  .contact{left:109px;top:4036px;font-size:24px;line-height:43px;color:var(--ink);font-style:normal}
  .contact .small{font-size:21px}
  .contact-rule{left:109px;top:4181px;width:974px;height:2px;background:#b9bcbb}
  .unsubscribe{right:117px;top:4198px;font-size:20px;color:var(--ink)}
</style>
</head>
<body>

<!-- hero -->
<div class="abs hero" role="img" aria-label="Photo of a bright retail store interior with shelves and a person walking by"></div>
<div class="abs brand hero-brand">RIDGEWAY</div>
<h1 class="abs hero-title"><span>We offer a time tested personal</span><br><span>and analytical process for</span><br><span>commercial insurance solutions</span></h1>

<!-- pillars -->
<section class="abs pillars">
  <div class="abs pillar" style="left:118px">
    <h3><svg width="26" height="28" viewBox="0 0 26 28"><circle cx="13" cy="7" r="6" fill="#fff"/><path d="M1 28c0-8 5-12 12-12s12 4 12 12z" fill="#fff"/></svg>COMPLIANCE</h3>
    <p>HR and safety onsite<br>compliance.<br>Onsite training and<br>programmes</p>
  </div>
  <div class="abs pillar" style="left:456px">
    <h3><svg width="32" height="26" viewBox="0 0 32 26"><rect x="1.5" y="1.5" width="29" height="23" rx="2" fill="none" stroke="#fff" stroke-width="3"/><rect x="6" y="7" width="9" height="7" fill="#fff"/><rect x="18" y="8" width="9" height="2.5" fill="#fff"/><rect x="6" y="17" width="21" height="2.5" fill="#fff"/></svg>PROFIT LEAKS</h3>
    <p>Premium Recovery Audit.<br>We detect and correct<br>profit leaks.<br>Incorrect class codes.</p>
  </div>
  <div class="abs pillar" style="left:800px">
    <h3><svg width="24" height="28" viewBox="0 0 24 28"><path d="M0 0h16l8 8v20H0z" fill="#fff"/><rect x="4" y="12" width="16" height="2.5" fill="#f26b35"/><rect x="4" y="18" width="16" height="2.5" fill="#f26b35"/></svg>CLAIMS</h3>
    <p>Injury and claims<br>management consulting.<br>&nbsp;We attend mediations on<br>your behalf.</p>
  </div>
</section>

<!-- panel -->
<div class="abs panel"></div>
<div class="abs intro">
  Hello,<br>
  Greetings. We are an insurance agency that specializes in lowering employers’ workers Comp cost.<br>
  We would like to kindly proposition you to refer to us your larger clients and prospects.<br>
  Our tried and tested programs and strategies will deliver the most effective combination of price and terms.
</div>
<div class="abs quote-mark" aria-hidden="true">”</div>

<h2 class="abs section-title">WHAT WE OFFER</h2>
<div class="abs section-rule"></div>

<div class="abs grid-line-h"></div>
<div class="abs grid-line-v" style="left:412px;top:1690px;height:765px"></div>
<div class="abs grid-line-v" style="left:779px;top:1690px;height:765px"></div>

<!-- row 1 -->
<div class="abs offer" style="left:97px;top:1700px">
  <h4>Our Mission</h4>
  <p style="margin-top:14px">Our mission is to reduce employers’ workers compensation costs.</p>
</div>
<div class="abs photo" style="left:97px;top:1817px;width:262px;height:183px;background:linear-gradient(180deg,#dfe5ea,#8c98a3 60%,#5b6670)" role="img" aria-label="City skyline photo"></div>

<div class="abs photo" style="left:465px;top:1696px;width:261px;height:180px;background:linear-gradient(180deg,#6e7174,#b9bbbc 55%,#4a4c4e)" role="img" aria-label="Open office interior photo"></div>
<div class="abs offer" style="left:465px;top:1918px">
  <h4>HR Services</h4>
  <p style="margin-top:18px">We can do it all - employmebt, compensation, benefits, employee compensation, and training.</p>
</div>

<div class="abs offer" style="left:838px;top:1700px">
  <h4>Safety Compliance</h4>
  <p style="margin-top:14px">We offer training in English and Spanish. Discount safety equipment, and drug test as low as $20.</p>
</div>
<div class="abs photo" style="left:838px;top:1817px;width:259px;height:183px;background:linear-gradient(180deg,#8fa3b5,#3b5f9a 55%,#2a3f6b)" role="img" aria-label="Photo of two workers in hard hats and blue uniforms"></div>

<!-- row 2 -->
<div class="abs offer" style="left:97px;top:2138px">
  <h4>Risk Management</h4>
  <p style="margin-top:12px">A holistic solution to manage risk, control loss, and improve compliance by creating effective risk mitigation programs.</p>
</div>
<div class="abs photo" style="left:97px;top:2255px;width:262px;height:179px;background:linear-gradient(180deg,#c7d3dd,#b7a06a 50%,#6b6f73)" role="img" aria-label="Construction site with cranes photo"></div>

<div class="abs photo" style="left:465px;top:2134px;width:261px;height:183px;background:linear-gradient(180deg,#e3e5e3,#b9c2bd 55%,#7d8f93)" role="img" aria-label="People meeting in a lounge photo"></div>
<div class="abs offer" style="left:465px;top:2347px">
  <h4>Work Comp Re-Audit</h4>
  <p style="margin-top:14px">We will guide you through your workers’ compensation audit while representing your interests.</p>
</div>

<div class="abs offer" style="left:838px;top:2138px">
  <h4>Premium Recovery</h4>
  <p style="margin-top:14px">Kick back while we lower your workers’ comp.</p>
</div>
<div class="abs photo" style="left:838px;top:2255px;width:259px;height:179px;background:linear-gradient(160deg,#d9d9d7,#9fa09e 55%,#5f6060)" role="img" aria-label="Hands working on a laptop photo"></div>

<!-- email draft -->
<section class="abs draft">
  <h2>ALREADY MADE EMAIL DRAFT</h2>
  <p>Follow this link for an already made email. You only need to input the names of the clients. Alternatively you can make your own email according to your preference.</p>
</section>
<a class="abs btn btn-solid">Email</a>

<!-- feature -->
<div class="abs feature-bg"></div>
<div class="abs feature"></div>
<div class="abs feature-photo" role="img" aria-label="Upward view of glass skyscrapers against the sky"></div>
<h2 class="abs feature-title">RIDGEWAY is the answer when it comes to Work Comp</h2>
<p class="abs feature-text">Is your company in compliance? Is your experience mode correct?<br>Do you have an out of control claim?</p>
<a class="abs btn btn-outline">More details</a>

<!-- footer -->
<footer>
  <div class="abs footer-band">
    <div class="abs brand footer-brand">RIDGEWAY</div>
    <span class="abs social" style="left:975px"></span>
    <span class="abs social" style="left:1032px"></span>
    <span class="abs social" style="left:1089px"></span>
  </div>
  <address class="abs contact">
    Contact Us<br>
    <span class="small">210 Marlow Rd, Suite 4, Brookfield, FL 33000</span><br>
    <span class="small">(555) 214 708</span>
  </address>
  <div class="abs contact-rule"></div>
  <a class="abs unsubscribe">unsubscribe</a>
</footer>

</body>
</html>
```